Brochure design for healthcare software company

We need a tri-fold brochure design for our healthcare software company that provides software and services for clinicians who manage patients who have or may be diagnosed with cancer.

We have an existing web, business card design and trade show booth design and want the ultimate design to be consistent with these. All of the files including stock images are provided.

Target Market(s)

Nurses, Healthcare professionals

Industry/Entity Type

Healthcare

Requirements
Must have
• Design consistent with attached tradeshow booth and business card.

```html
<!DOCTYPE html>
<html lang="en">
<head>
<meta charset="utf-8">
<title>Carevia Navigation – Brochure Inside Spread</title>
<link rel="stylesheet" href="https://fonts.googleapis.com/css2?family=Nanum+Gothic:wght@400;700&display=swap">
<style>
  :root {
    --page-bg: #ffffff;
    --frame-line: #111111;
    --brand-green: #5fb36a;
    --brand-blue: #0b4ea2;
    --text: #1e1e1e;
    --photo-keyboard: #cfcac8;
    --photo-keyboard-dark: #9a9290;
    --photo-office: #8fbfcc;
    --photo-office-dark: #3e6f80;
    --photo-analytics: #e8eef5;
    --photo-analytics-blue: #5a9bd8;
    --photo-files: #d9c7a3;
    --photo-files-dark: #a88c5c;
  }
  html, body {
    margin: 0;
    padding: 0;
    width: 1200px;
    height: 1000px;
    overflow: hidden;
    background: var(--page-bg);
    font-family: "Nanum Gothic", sans-serif;
    color: var(--text);
  }
  .spread {
    position: absolute;
    left: 46px;
    top: 117px;
    width: 1104px;
    height: 781px;
    border: 1px solid var(--frame-line);
    box-sizing: border-box;
    overflow: hidden;
    background: var(--page-bg);
  }
  .spread-art {
    position: absolute;
    left: 0;
    top: 0;
    width: 1104px;
    height: 781px;
  }
  .feature {
    position: absolute;
  }
  .feature h2 {
    margin: 0 0 11px;
    font-size: 16.5px;
    font-weight: 400;
    letter-spacing: 0.4px;
  }
  .feature p {
    margin: 0;
    font-size: 11.6px;
    line-height: 16.2px;
    letter-spacing: 0.15px;
  }
  .feature--navigation { left: 22px; top: 131px; width: 335px; }
  .feature--workflow   { left: 21px; top: 314px; width: 325px; }
  .feature--reporting  { left: 394px; top: 314px; width: 320px; }
  .feature--paper      { left: 762px; top: 314px; width: 300px; }
  .feature--integrated { left: 762px; top: 470px; width: 290px; }
</style>
</head>
<body>
  <main class="spread">
    <svg class="spread-art" viewBox="0 0 1104 781" xmlns="http://www.w3.org/2000/svg">
      <defs>
        <linearGradient id="keyboardTone" x1="0" y1="0" x2="1" y2="1">
          <stop offset="0" stop-color="var(--photo-keyboard-dark)"/>
          <stop offset="0.5" stop-color="var(--photo-keyboard)"/>
          <stop offset="1" stop-color="#e4e2e2"/>
        </linearGradient>
        <linearGradient id="officeTone" x1="0" y1="0" x2="1" y2="1">
          <stop offset="0" stop-color="var(--photo-office-dark)"/>
          <stop offset="1" stop-color="var(--photo-office)"/>
        </linearGradient>
        <linearGradient id="analyticsTone" x1="0" y1="0" x2="0" y2="1">
          <stop offset="0" stop-color="var(--photo-analytics)"/>
          <stop offset="1" stop-color="var(--photo-analytics-blue)"/>
        </linearGradient>
        <linearGradient id="filesTone" x1="0" y1="0" x2="0" y2="1">
          <stop offset="0" stop-color="var(--photo-files)"/>
          <stop offset="1" stop-color="var(--photo-files-dark)"/>
        </linearGradient>
        <clipPath id="lowerPhotoArea">
          <path d="M0,500 C300,498 560,560 760,660 C900,730 1020,768 1104,782 L1104,781 L0,781 Z"/>
        </clipPath>
      </defs>

      <!-- top hero image area -->
      <path role="img" aria-label="Photo: hands typing on a laptop keyboard"
            fill="url(#keyboardTone)"
            d="M110,0 L1104,0 L1104,266 C880,266 640,262 500,222 C360,180 250,60 110,0 Z"/>
      <!-- top wave stripes -->
      <path d="M0,0 C200,2 340,150 500,214 C650,268 880,264 1104,262"
            fill="none" stroke="var(--brand-green)" stroke-width="10"/>
      <path d="M150,40 C300,110 390,200 510,232 C660,278 890,280 1104,282"
            fill="none" stroke="var(--brand-blue)" stroke-width="14"/>

      <!-- lower image strip -->
      <g clip-path="url(#lowerPhotoArea)">
        <rect role="img" aria-label="Photo: nurse working at a laptop in a clinic"
              x="0" y="480" width="371" height="301" fill="url(#officeTone)"/>
        <rect role="img" aria-label="Illustration: tablet showing analytics charts"
              x="371" y="480" width="369" height="301" fill="url(#analyticsTone)"/>
        <rect role="img" aria-label="Photo: stack of paper files and folders"
              x="740" y="480" width="364" height="301" fill="url(#filesTone)"/>
      </g>
      <!-- lower wave band -->
      <path fill="var(--brand-green)"
            d="M0,475 C300,470 580,540 780,640 C920,712 1030,760 1104,776
               L1104,782 C1020,768 900,730 760,660 C560,560 300,498 0,500 Z"/>
    </svg>

    <section class="feature feature--navigation">
      <h2>Simplified navigation</h2>
      <p>Track all of your patients from their entry point, for example an abnormal screening exam or a positive diagnosis, through survivorship. Carevia Navigation allows you to easily maintain a record of all referrals, exams, treatments, contacts, appointments and notes for your patients.</p>
    </section>

    <section class="feature feature--workflow">
      <h2>Advanced workflow tools</h2>
      <p>View and manage your entire patient load in a single dynamic work list area. Completely customizable to match your workflow. Create checklists for every step of your workflow to maintain consistent patient care and monitoring.</p>
    </section>

    <section class="feature feature--reporting">
      <h2>Reporting and analytics</h2>
      <p>Quickly demonstrate the value of your navigation efforts with deep analytics and reporting. View current and historical trends for any or all of your facilities and staff, including detailed reporting on work loads, time to care, patient barriers, referrals and appointments.</p>
    </section>

    <section class="feature feature--paper">
      <h2>Eliminate paper</h2>
      <p>Manage all of your paperwork and patient forms in one easy to use area. Automatically create document packets and auto fill forms for patients or referrals with a single click.</p>
    </section>

    <section class="feature feature--integrated">
      <h2>Integrated</h2>
      <p>Reduce double data entry by integrating the systems you already have. Patients can be seamlessly added and updated without manual efforts.</p>
    </section>
  </main>
</body>
</html>
```